The Lantern Assembly Pitchdeck Template

The Lantern Assembly would like a branded pitch deck template design for members to use when presenting their projects and proposals. The deck should include 10-15 different slide designs, each with the same branded theme, but with a variety of icon graphics and other design features that will empower members to easily create a beautiful pitch deck just by adding written content.

Please visit thelantern.org to get a sense for our branding - purple, space, galaxy, white font and the planetary logo are some commonalities.

Here are 2 google drive links with some additional designs

https://files.cloudnestbox.net/share/u/1/dir/8KpqZr3Tn5Yb-wLxVd2Hc-Qm4jEsAf7Ug

https://files.cloudnestbox.net/share/u/1/dir/6Rtb2-Lm9Xc4-hNwq813Fvkzpe_Jd7Sa

```html
<!DOCTYPE html>
<html lang="en">
<head>
<meta charset="utf-8">
<title>The Lantern Assembly — Pitch Deck Template</title>
<link rel="stylesheet" href="https://fonts.googleapis.com/css2?family=Montserrat:ital,wght@0,300;0,400;0,500;0,600;0,700;0,800;1,700;1,800&display=swap">
<style>
:root{
  --page:#ffffff;
  --ink:#000000;
  --white:#ffffff;
  --mute:#8c8a92;
  --dim:#5c5a62;
  --card:#18171c;
  --band:#25242b;
  --purple:#8a6fc0;
  --lavender:#a996d8;
  --violet:#6b2fb3;
  --plum:#4a3570;
  --grey:#7a787f;
}
*{margin:0;padding:0;box-sizing:border-box}
html,body{width:853px;height:1200px;overflow:hidden;background:var(--page)}
body{font-family:"Montserrat",sans-serif;color:var(--white)}
.deck{position:absolute;left:3px;top:28px;display:grid;grid-template-columns:repeat(3,279px);grid-auto-rows:157px;column-gap:5px;row-gap:5.5px}
.slide{position:relative;background:var(--ink);overflow:hidden}
.abs{position:absolute}
.ph{position:absolute}
.title{position:absolute;left:31px;top:14px;font-size:10.5px;font-weight:300;letter-spacing:.1px;white-space:nowrap}
.title.center{left:0;right:0;text-align:center}
.tiny{font-size:3px;line-height:4.6px;color:var(--mute)}
.legal{position:absolute;left:31px;bottom:7px;font-size:2px;color:var(--dim)}
.rail{position:absolute;left:11px;top:45px;width:8px;height:75px}
.rail .mark{position:absolute;left:1px;top:0;width:6px;height:6px;border:1px solid var(--white);border-radius:50%}
.rail .line{position:absolute;left:4px;top:10px;width:.5px;height:55px;background:#6a6870}
.rail .dot{position:absolute;left:3px;top:72px;width:2px;height:2px;background:#8a8890;border-radius:50%}
.brandname{position:absolute;left:0;right:0;text-align:center;font-weight:700;color:var(--white)}
.ring{position:absolute;border:1.2px solid var(--white);border-radius:50%}
.section-kicker{position:absolute;font-style:italic;font-weight:800;color:var(--purple);font-size:13px}
.section-head{position:absolute;font-style:italic;font-weight:800;color:var(--white);font-size:23px;letter-spacing:-.3px;white-space:nowrap}
.card-white{position:absolute;background:var(--white);color:#333}
.card-dark{position:absolute;background:var(--card)}
.card-year{font-size:2.6px;color:#555;position:absolute;left:5px;top:5px}
.card-name{font-size:6.5px;font-weight:400;position:absolute;left:5px;top:11px;letter-spacing:.1px}
.card-text{font-size:2.4px;line-height:3.6px;position:absolute;left:5px;top:24px;width:115px;color:#9a98a0}
.arrow{position:absolute;width:8px;height:8px;border-radius:50%;background:var(--white)}
.arrow::after{content:"";position:absolute;left:2.5px;top:2.6px;width:2px;height:2px;border-top:.8px solid #000;border-right:.8px solid #000;transform:rotate(45deg)}
.tag{position:absolute;font-size:3.8px;font-weight:600;display:flex;align-items:center;justify-content:center;color:var(--white)}
.tag .ico{position:absolute;top:-4px;right:-4px;width:7px;height:7px;border-radius:50%;background:var(--white);border:1px solid var(--plum)}
.point{position:absolute;left:201px;width:64px;height:21px;background:#6e5b9c}
.point b{position:absolute;left:14px;top:4px;font-size:4px;font-weight:700}
.point i{position:absolute;left:14px;top:12px;font-size:2.4px;font-style:normal}
.point i::before{content:"";display:inline-block;width:2px;height:2px;border-radius:50%;background:#fff;margin-right:3px}
.point .sq{position:absolute;left:-3px;top:-5px;width:9px;height:9px;background:#3d3258;border:.6px solid #fff}
.proc{position:absolute;left:32px;height:6px;font-size:3.2px;display:flex;align-items:center;padding-left:9px}
.core{position:absolute;left:133px;top:73px;width:34px;height:34px;border-radius:50%;background:#222126;text-align:center}
.core b{display:block;font-size:4px;font-weight:700;margin-top:11px}
.core span{display:block;font-size:2.4px;line-height:3.6px;color:#c9c7cf;margin-top:1px}
</style>
</head>
<body>
<main class="deck">

  <!-- 1 Cover -->
  <section class="slide cover">
    <div class="ph" role="img" aria-label="Deep starfield with a faint purple nebula" style="inset:0;background:radial-gradient(ellipse at 35% 30%,#3a2b48 0%,#1a1420 35%,#070609 75%)"></div>
    <div class="ring" style="left:130px;top:32px;width:18px;height:18px"></div>
    <div class="abs" style="left:139px;top:60px;width:.5px;height:24px;background:#8a8890"></div>
    <div class="brandname" style="top:92px;font-size:15.5px;letter-spacing:.2px">THE LANTERN ASSEMBLY</div>
    <div class="abs" style="left:0;right:0;top:118px;text-align:center;font-size:7.2px;font-weight:300">UNITING HUMANITY AS ONE</div>
  </section>

  <!-- 2 Cover alt -->
  <section class="slide cover-alt">
    <div class="ph" role="img" aria-label="Night sky with a line of planets above a mountain silhouette and glowing rings" style="inset:0;background:radial-gradient(ellipse at 50% 55%,#5b4c7c 0%,#33284e 40%,#141122 80%),linear-gradient(#1b1a35,#2a1f3a)"></div>
    <div class="ph" role="img" aria-label="Mountain silhouette" style="left:0;right:0;bottom:0;height:45px;background:linear-gradient(#3a2c48,#1b1525)"></div>
    <div class="brandname" style="top:59px;font-size:14.5px">THE LANTERN ASSEMBLY</div>
    <div class="abs" style="left:0;right:0;top:86px;text-align:center;font-size:7.2px;font-weight:300">UNITING HUMANITY AS ONE</div>
    <div class="ring" style="left:131px;top:107px;width:16px;height:16px"></div>
    <div class="abs" style="left:139px;top:136px;width:.5px;height:21px;background:#9a98a0"></div>
  </section>

  <!-- 3 Image and Text -->
  <section class="slide">
    <div class="rail"><span class="mark"></span><span class="line"></span><span class="dot"></span></div>
    <h2 class="title" style="top:24px">Image and Text</h2>
    <p class="abs" style="left:32px;top:38px;font-size:4px;font-weight:600;color:var(--purple)">We're Engineers Developing A Massive Space Station With Artificial Spin Gravity</p>
    <div class="ph" role="img" aria-label="Banner of a purple cosmic face with a brand name" style="left:32px;top:48px;width:214px;height:42px;background:linear-gradient(90deg,#3b2a8a,#7a3fc0 50%,#4a2c9a)"></div>
    <div class="abs" style="left:32px;top:57px;width:214px;text-align:center;font-size:15px;font-weight:700;letter-spacing:3px">ORRIN</div>
    <div class="abs" style="left:32px;top:78px;width:214px;text-align:center;font-size:2.6px;letter-spacing:1.4px">QUIET ORBIT</div>
    <p class="abs tiny" style="left:33px;top:95px;width:212px;color:#c9c7cf">Every project we share begins with a question about the sky above us and the people below it. We gather to listen, to build and to learn together in open rooms. Our members bring plans for schools, gardens, studios and outreach, and this space lets each idea speak plainly. Add your own words here to describe the work, the need it meets and the people it serves, then keep the rest of the slide calm and clear for the audience.</p>
    <p class="legal">room for a legal notice here</p>
  </section>

  <!-- 4 Image and Bullets -->
  <section class="slide">
    <div class="rail"><span class="mark"></span><span class="line"></span><span class="dot"></span></div>
    <h2 class="title">Image and Bullets Text</h2>
    <div class="ph" role="img" aria-label="Person sitting on a rock above the curve of the Earth" style="left:32px;top:38px;width:107px;height:91px;background:linear-gradient(#0b1a2e 0%,#2d5b86 30%,#c9cdd2 48%,#8a7a6a 75%,#4a3a2e)"></div>
    <p class="abs" style="left:148px;top:44px;width:110px;font-size:4.2px;font-weight:600;color:var(--purple);line-height:5.4px">We're Engineers Developing A Massive Space Station With Artificial Spin Gravity</p>
    <ul class="abs tiny" style="left:148px;top:62px;width:116px;list-style:none;color:#c9c7cf;line-height:4.4px">
      <li style="margin-bottom:3px">• Share the aim of your project in one line and say who it helps most.</li>
      <li style="margin-bottom:3px">• Name the steps you will take and the time each one will need to finish.</li>
      <li style="margin-bottom:3px">• List the people and partners who will carry the work forward with you.</li>
      <li>• Close with the support you are asking the assembly to give.</li>
    </ul>
    <p class="legal">room for a legal notice here</p>
  </section>

  <!-- 5 Image and Big Text -->
  <section class="slide">
    <div class="rail"><span class="mark"></span><span class="line"></span><span class="dot"></span></div>
    <h2 class="title">Image and Big Text</h2>
    <div class="abs" style="left:32px;top:35px;width:238px;height:17px;border:1px solid #3b2f6e;display:flex;align-items:center;justify-content:center;font-size:4.6px">THE LANTERN ASSEMBLY UNITING HUMANITY AS ONE</div>
    <div class="ph" role="img" aria-label="Lone figure on dunes beneath a teal galaxy" style="left:32px;top:59px;width:238px;height:68px;background:linear-gradient(#0c2a44 0%,#1b7a9a 30%,#0e2a3e 55%,#3b2a3e 80%,#5a3c4a)"></div>
    <p class="legal">room for a legal notice here</p>
  </section>

  <!-- 6 Who Are We -->
  <section class="slide">
    <div class="ph" role="img" aria-label="Hand reaching toward a floating glass prism filled with a galaxy" style="inset:0;background:radial-gradient(ellipse at 55% 25%,#3a7ab0 0%,#1a3a6a 35%,#0c1a34 70%),linear-gradient(#0d1a33,#1f3c3a)"></div>
    <div class="abs" style="left:5px;font-size:4px;letter-spacing:1px;transform:rotate(-90deg);transform-origin:left top;top:58px">VAST</div>
    <div class="abs" style="left:11px;top:62px;width:.5px;height:55px;background:#8a8890"></div>
    <h3 class="abs" style="left:179px;top:57px;font-size:6.5px;font-weight:700">WHO ARE WE</h3>
    <p class="abs tiny" style="left:180px;top:70px;width:82px;color:#d6d4dc;line-height:4.4px">We are a gathering of people who look up together. We meet to share ideas, support one another and bring new projects to life, helping each member carry a small light out into the wider world.</p>
    <p class="legal">room for a legal notice here</p>
  </section>

  <!-- 7 Graphs / Charts -->
  <section class="slide">
    <div class="rail"><span class="mark"></span><span class="line"></span><span class="dot"></span></div>
    <h2 class="title" style="top:24px">Graphs / Charts</h2>
    <div class="abs" style="left:134px;top:42px;font-size:4.8px">Chart Title</div>
    <div class="abs" style="left:124px;top:52px;font-size:2.8px;color:#c9c7cf"><span style="color:#5b3f86">●</span>Series 1 &nbsp;<span style="color:#e0dbe9">●</span>Series 2 &nbsp;<span style="color:#9c86cc">●</span>Series 3</div>
    <svg class="abs" style="left:30px;top:57px" width="245" height="90" viewBox="0 0 245 90">
      <g stroke="#3a3940" stroke-width=".5">
        <line x1="8" y1="8" x2="240" y2="8"/><line x1="8" y1="19.5" x2="240" y2="19.5"/><line x1="8" y1="31" x2="240" y2="31"/><line x1="8" y1="42.5" x2="240" y2="42.5"/><line x1="8" y1="54" x2="240" y2="54"/><line x1="8" y1="65.5" x2="240" y2="65.5"/><line x1="8" y1="77" x2="240" y2="77"/>
      </g>
      <g fill="#c9c7cf" font-size="3" font-family="Montserrat, sans-serif">
        <text x="3" y="9">6</text><text x="3" y="20.5">5</text><text x="3" y="32">4</text><text x="3" y="43.5">3</text><text x="3" y="55">2</text><text x="3" y="66.5">1</text>
        <text x="8" y="84">0</text><text x="31" y="84">0.5</text><text x="54" y="84">1</text><text x="77" y="84">1.5</text><text x="100" y="84">2</text><text x="123" y="84">2.5</text><text x="146" y="84">3</text><text x="169" y="84">3.5</text><text x="192" y="84">4</text><text x="215" y="84">4.5</text><text x="237" y="84">5</text>
      </g>
      <circle cx="55" cy="27" r="8.5" fill="#4a2f6e"/>
      <circle cx="55" cy="49" r="8.5" fill="#e3deea"/>
      <circle cx="55" cy="54" r="8.5" fill="#9a80cc"/>
      <circle cx="101" cy="25" r="8.5" fill="#e3deea"/>
      <circle cx="101" cy="48" r="8.5" fill="#4a2f6e"/>
      <circle cx="101" cy="54" r="8.5" fill="#9a80cc"/>
      <circle cx="147" cy="37" r="8.5" fill="#4a2f6e"/>
      <circle cx="147" cy="43" r="8.5" fill="#9a80cc"/>
      <circle cx="147" cy="57" r="8.5" fill="#e3deea"/>
      <circle cx="193" cy="14" r="8.5" fill="#9a80cc"/>
      <circle cx="193" cy="21" r="8.5" fill="#8a70bd"/>
      <circle cx="193" cy="45" r="8.5" fill="#e3deea"/>
    </svg>
    <p class="legal">room for a legal notice here</p>
  </section>

  <!-- 8 Meet the Experts -->
  <section class="slide">
    <div class="rail"><span class="mark"></span><span class="line"></span><span class="dot"></span></div>
    <h2 class="title">Meet Orrin Expert</h2>
    <div class="ph" role="img" aria-label="Portrait of team member one" style="left:32px;top:40px;width:43px;height:43px;border-radius:50%;background:linear-gradient(#e7e2dc,#8a6a54)"></div>
    <div class="ph" role="img" aria-label="Portrait of team member two" style="left:113px;top:40px;width:43px;height:43px;border-radius:50%;background:linear-gradient(#4c5a48,#2a3226)"></div>
    <div class="ph" role="img" aria-label="Portrait of team member three" style="left:192px;top:40px;width:43px;height:43px;border-radius:50%;background:linear-gradient(#1d4a7a,#2a6ab0)"></div>
    <div class="abs" style="left:32px;top:95px;width:70px"><b style="font-size:3.5px;font-weight:700">NAME SURNAME</b><p style="font-size:3px;color:var(--mute)">Founder and Ceo</p><p class="tiny" style="margin-top:3px;color:#c9c7cf;line-height:3.8px">A short note about this member, their role and the work they lead for the assembly today.</p></div>
    <div class="abs" style="left:113px;top:95px;width:70px"><b style="font-size:3.5px;font-weight:700">NAME SURNAME</b><p style="font-size:3px;color:var(--mute)">Founder and Ceo</p><p class="tiny" style="margin-top:3px;color:#c9c7cf;line-height:3.8px">A short note about this member, their role and the work they lead for the assembly today.</p></div>
    <div class="abs" style="left:192px;top:95px;width:70px"><b style="font-size:3.5px;font-weight:700">NAME SURNAME</b><p style="font-size:3px;color:var(--mute)">Founder and Ceo</p><p class="tiny" style="margin-top:3px;color:#c9c7cf;line-height:3.8px">A short note about this member, their role and the work they lead for the assembly today.</p></div>
    <p class="legal">room for a legal notice here</p>
  </section>

  <!-- 9 About -->
  <section class="slide">
    <div class="rail"><span class="mark"></span><span class="line"></span><span class="dot"></span></div>
    <h2 class="title center" style="top:17px;padding-left:20px">About Our Company</h2>
    <div class="abs" style="left:35px;top:36px;width:208px;height:40px;background:var(--card);text-align:center">
      <p style="font-size:4.8px;margin-top:11px">YOUR UNIVERSE TEXT HERE</p>
      <p class="tiny" style="width:180px;margin:1px auto 0;color:#c9c7cf;line-height:3.8px">Tell the story of the assembly in two calm lines: where it began, who it serves and the hope that keeps members gathering each season together.</p>
    </div>
    <div class="abs" style="left:35px;top:94px;width:208px;height:.5px;background:#3a3940"></div>
    <div class="abs" style="left:35px;top:86px;width:208px;display:flex;justify-content:space-between;font-size:3.8px;color:#c9c7cf"><span>2014</span><span>2015</span><span>2016</span><span>2017</span><span style="color:#fff">PRESENT</span></div>
    <div class="abs" style="left:0;right:0;top:106px;bottom:0;background:var(--band)"></div>
    <div class="ph" role="img" aria-label="Spiral galaxy" style="left:35px;top:116px;width:50px;height:33px;background:radial-gradient(#c7a8ff,#5b3aa8 45%,#1a1440)"></div>
    <div class="ph" role="img" aria-label="Pink glowing rift in space" style="left:88px;top:116px;width:50px;height:33px;background:radial-gradient(#ff8ad8,#7a2a7a 40%,#1a0e2a)"></div>
    <div class="ph" role="img" aria-label="Planet horizon with orange nebula" style="left:140px;top:116px;width:50px;height:33px;background:radial-gradient(circle at 50% 80%,#e88a5a,#6a3a7a 50%,#1a1230)"></div>
    <div class="ph" role="img" aria-label="Close-up of an eye reflecting a galaxy" style="left:193px;top:116px;width:50px;height:33px;background:radial-gradient(#c9d4e6,#4a5a7a 40%,#2a1a18)"></div>
  </section>

  <!-- 10 Gallery -->
  <section class="slide">
    <div class="rail"><span class="mark"></span><span class="line"></span><span class="dot"></span></div>
    <div class="ph" role="img" aria-label="Galaxy pattern in the shape of lungs" style="left:49px;top:18px;width:65px;height:51px;background:linear-gradient(120deg,#5a7aa8,#c9d0e0 50%,#6a4a8a)"></div>
    <div class="ph" role="img" aria-label="Glowing crack in dark rock" style="left:32px;top:73px;width:48px;height:48px;background:linear-gradient(135deg,#4a5a6a,#c24a7a 50%,#2a2a3a)"></div>
    <div class="ph" role="img" aria-label="Nebula fragment" style="left:66px;top:106px;width:32px;height:33px;background:radial-gradient(#b9a0d8,#3a2a5a)"></div>
    <div class="ph" role="img" aria-label="Black hole with a bright accretion ring" style="left:188px;top:16px;width:49px;height:48px;background:radial-gradient(circle,#000 15%,#e8e0f0 22%,#3a5a9a 45%,#0d1a3a)"></div>
    <div class="abs" style="left:224px;top:47px;width:31px;height:31px;background:var(--purple);text-align:center">
      <p style="font-size:14px;font-weight:700;line-height:18px;margin-top:3px">22</p>
      <p style="font-size:3.6px">JUNE</p>
    </div>
    <h3 class="abs" style="left:128px;top:80px;font-size:9px;font-weight:300;line-height:10px">Universe Image<br>Gallery</h3>
    <p class="abs" style="left:128px;top:110px;font-size:4.8px;color:var(--purple)">NATIONAL universe 2022</p>
    <p class="abs tiny" style="left:128px;top:118px;width:110px;color:#c9c7cf;line-height:4.2px">A gallery of moments from our gatherings, shared so members can see the work and the people behind each project.</p>
  </section>

  <!-- 11 Timeline -->
  <section class="slide">
    <div class="rail"><span class="mark"></span><span class="line"></span><span class="dot"></span></div>
    <h2 class="abs" style="left:59px;top:17px;font-size:9px;font-weight:300;line-height:10px">COMPANY TIMELINE<br>EVENT</h2>
    <div class="abs" style="left:36px;top:55px;width:.5px;height:102px;background:#3a3940"></div>
    <span class="arrow" style="left:32px;top:72px"></span>
    <span class="abs" style="left:33px;top:113px;font-size:5px;color:#fff">›</span>
    <div class="card-white" style="left:60px;top:58px;width:132px;height:36px">
      <span class="card-year">2022</span><span class="card-name">VENICE SHOW</span>
      <p class="card-text">A short line about this event, where it was held and what the members shared there.</p>
    </div>
    <div class="ph" role="img" aria-label="Glowing orange planet" style="left:192px;top:58px;width:51px;height:36px;background:radial-gradient(circle at 45% 50%,#f0a060,#8a3a2a 45%,#1a1010)"></div>
    <div class="card-dark" style="left:60px;top:100px;width:132px;height:36px;color:#fff">
      <span class="card-year" style="color:#bbb">2022</span><span class="card-name">BARCELONA EVENT</span>
      <p class="card-text" style="color:#c9c7cf">A short line about this event, where it was held and what the members shared there.</p>
    </div>
    <div class="ph" role="img" aria-label="Figure on dunes beneath a teal galaxy" style="left:192px;top:100px;width:51px;height:36px;background:linear-gradient(#0e3a5a,#1a8ab0 40%,#3a2a3a)"></div>
  </section>

  <!-- 12 Events -->
  <section class="slide">
    <div class="rail"><span class="mark"></span><span class="line"></span><span class="dot"></span></div>
    <div class="abs" style="left:38px;top:0;width:.5px;height:157px;background:#2a2930"></div>
    <span class="arrow" style="left:35px;top:34px"></span>
    <span class="arrow" style="left:35px;top:77px"></span>
    <div class="card-white" style="left:59px;top:20px;width:132px;height:37px">
      <span class="card-year">2023</span><span class="card-name">LONDON SHOW</span>
      <p class="card-text">A short line about this event, where it was held and what the members shared there.</p>
    </div>
    <div class="ph" role="img" aria-label="Orange nebula over a small figure" style="left:191px;top:20px;width:52px;height:37px;background:radial-gradient(circle at 50% 40%,#f2a262,#7a3a2e 50%,#1a1012)"></div>
    <div class="card-white" style="left:59px;top:63px;width:132px;height:37px">
      <span class="card-year">2023</span><span class="card-name">SPRING CONFERENCE</span>
      <p class="card-text">A short line about this event, where it was held and what the members shared there.</p>
    </div>
    <div class="ph" role="img" aria-label="Teal galaxy above a desert" style="left:191px;top:63px;width:52px;height:37px;background:linear-gradient(#0e3a5a,#1a8ab0 45%,#2a2030)"></div>
    <svg class="abs" style="left:62px;top:115px" width="10" height="10" viewBox="0 0 10 10"><path d="M5 0 L5.6 4.4 L10 5 L5.6 5.6 L5 10 L4.4 5.6 L0 5 L4.4 4.4 Z" fill="#9a86d8"/></svg>
    <p class="abs" style="left:76px;top:117px;font-size:4.2px">YOUR &nbsp;TEXT HERE</p>
    <p class="abs tiny" style="left:76px;top:123px;width:186px;color:#c9c7cf;line-height:3.8px">Use this space for a closing note on the season of events, the members who took part and what the assembly plans to host next year together.</p>
  </section>

  <!-- 13 Section 01 -->
  <section class="slide">
    <div class="ph" role="img" aria-label="Rocky cliffs meeting a purple cosmic cloud" style="left:15px;top:33px;width:250px;height:58px;background:linear-gradient(90deg,#3a3638,#5a5460 35%,#6a5a8a 60%,#3a3a4a)"></div>
    <p class="section-kicker" style="left:15px;top:64px">SECTION 01</p>
    <h2 class="section-head" style="left:31px;top:78px">SECTION BREAK</h2>
  </section>

  <!-- 14 More Plan -->
  <section class="slide">
    <div class="rail"><span class="mark"></span><span class="line"></span><span class="dot"></span></div>
    <div class="ph" role="img" aria-label="Purple nebula above desert dunes" style="left:32px;top:30px;width:232px;height:95px;background:linear-gradient(100deg,#2a2030,#4a3a5a 35%,#3a2a4a 60%,#6a5a7a)"></div>
    <div class="abs" style="left:164px;top:18px;width:86px;height:101px;background:#4e3a7a"></div>
    <div class="ph" role="img" aria-label="Close-up of an eye reflecting a galaxy" style="left:176px;top:9px;width:64px;height:51px;background:radial-gradient(#d0dbe8,#5a6a8a 35%,#3a2a2a 70%)"></div>
    <div class="ph" role="img" aria-label="Pink glowing rift in space" style="left:176px;top:64px;width:64px;height:62px;background:radial-gradient(#ff9ae0,#7a2a8a 40%,#1a1040)"></div>
    <div class="abs" style="left:184px;top:111px;width:43px;height:21px;background:#9f8bcc;text-align:center">
      <p style="font-size:7.5px;font-weight:600;margin-top:3px">23.635</p>
      <p style="font-size:2.8px">Time exploring</p>
    </div>
    <span class="abs" style="left:180px;top:108px;width:5px;height:5px;border-radius:50%;background:#fff"></span>
    <h3 class="abs" style="left:46px;top:52px;font-size:9px;font-weight:300;line-height:10px">More Plan for<br>Explore New</h3>
    <p class="abs tiny" style="left:46px;top:79px;width:90px;color:#c9c7cf;line-height:4.2px">A quiet season of planning has led us here, with new ideas ready to share and a whole team eager to begin.</p>
  </section>

  <!-- 15 Mock Up -->
  <section class="slide">
    <div class="rail"><span class="mark"></span><span class="line"></span><span class="dot"></span></div>
    <h2 class="title center" style="top:17px;padding-left:10px">Mock Up Slide</h2>
    <div class="abs" style="left:55px;top:37px;width:168px;height:9px;background:#fff;border-radius:1px">
      <span class="abs" style="left:4px;top:3.2px;font-size:0;"><i style="display:inline-block;width:2.5px;height:2.5px;border-radius:50%;background:#333;margin-right:1px"></i><i style="display:inline-block;width:2.5px;height:2.5px;border-radius:50%;background:#333;margin-right:1px"></i><i style="display:inline-block;width:2.5px;height:2.5px;border-radius:50%;background:#333"></i></span>
      <span class="abs" style="left:22px;top:2px;width:82px;height:5px;background:#eee;font-size:2px;color:#aaa;padding-left:3px;line-height:5px">http://www.site.com</span>
    </div>
    <div class="ph" role="img" aria-label="Silhouette of a person under a purple and pink cloud in a starry sky" style="left:55px;top:46px;width:168px;height:90px;background:linear-gradient(#1a1420,#6a2a5a 25%,#3a2a4a 50%,#8a6a5a 80%,#2a2018)"></div>
    <div class="abs" style="left:203px;top:52px;width:58px;height:67px;background:#8b73c4;text-align:center">
      <svg class="abs" style="left:15px;top:6px" width="28" height="28" viewBox="0 0 28 28"><circle cx="14" cy="14" r="12" fill="none" stroke="#b7a6e0" stroke-width="1.2"/><path d="M14 2 A12 12 0 1 1 4.5 21.3" fill="none" stroke="#fff" stroke-width="1.2"/><text x="14" y="16.5" text-anchor="middle" font-size="7" fill="#fff" font-family="Montserrat, sans-serif">61%</text></svg>
      <p style="font-size:4px;margin-top:40px">UNIVERSE</p>
      <p class="tiny" style="width:44px;margin:1px auto 0;color:#eee;line-height:3.6px">Share one figure your project is proud of.</p>
    </div>
    <div class="abs" style="left:37px;top:108px;font-size:4px;line-height:11px;color:#c9c7cf">01<br>02<br>03</div>
  </section>

  <!-- 16 Section 02 -->
  <section class="slide">
    <div class="ph" role="img" aria-label="Sunset clouds with a ringed planet and orbit lines" style="inset:0;background:linear-gradient(#6a5a6a 0%,#a8634a 25%,#5a3a4a 55%,#1a1014 100%)"></div>
    <p class="section-kicker" style="left:26px;top:79px">SECTION 02</p>
    <h2 class="section-head" style="left:32px;top:93px">BREAK SLIDE</h2>
  </section>

  <!-- 17 Molecular -->
  <section class="slide">
    <div class="rail"><span class="mark"></span><span class="line"></span><span class="dot"></span></div>
    <h2 class="title">Molecular Diagram</h2>
    <div class="ph" role="img" aria-label="Atom illustration with three crossing orbits and small nodes around a central circle" style="left:102px;top:42px;width:96px;height:96px;border-radius:50%;background:radial-gradient(circle,#2a2830 0%,#17161b 55%,#000 72%)"></div>
    <div class="core"><b>Description</b><span>A wonderful calm has<br>taken hold</span></div>
    <div class="tag" style="left:53px;top:45px;width:49px;height:13px;background:var(--grey)">Molecular I<span class="ico"></span></div>
    <div class="tag" style="left:195px;top:45px;width:51px;height:13px;background:var(--plum)">Molecular II<span class="ico" style="left:-4px;right:auto"></span></div>
    <div class="tag" style="left:32px;top:80px;width:49px;height:13px;background:var(--plum)">Molecular VI<span class="ico"></span></div>
    <div class="tag" style="left:217px;top:80px;width:51px;height:13px;background:var(--purple)">Molecular III<span class="ico" style="left:-4px;right:auto"></span></div>
    <div class="tag" style="left:53px;top:116px;width:49px;height:13px;background:var(--violet)">Molecular V<span class="ico"></span></div>
    <div class="tag" style="left:195px;top:116px;width:51px;height:13px;background:var(--plum)">Molecular IV<span class="ico" style="left:-4px;right:auto"></span></div>
  </section>

  <!-- 18 Chart & Points -->
  <section class="slide">
    <div class="rail"><span class="mark"></span><span class="line"></span><span class="dot"></span></div>
    <h2 class="title">Chart &amp; Points</h2>
    <svg class="abs" style="left:28px;top:44px" width="150" height="100" viewBox="0 0 150 100">
      <g stroke="#3a3940" stroke-width=".5">
        <line x1="8" y1="3" x2="146" y2="3"/><line x1="8" y1="12.5" x2="146" y2="12.5"/><line x1="8" y1="22" x2="146" y2="22"/><line x1="8" y1="31.5" x2="146" y2="31.5"/><line x1="8" y1="41" x2="146" y2="41"/><line x1="8" y1="50.5" x2="146" y2="50.5"/><line x1="8" y1="60" x2="146" y2="60"/><line x1="8" y1="69.5" x2="146" y2="69.5"/><line x1="8" y1="79" x2="146" y2="79"/>
      </g>
      <g fill="#c9c7cf" font-size="3" font-family="Montserrat, sans-serif">
        <text x="2" y="4">8</text><text x="2" y="13.5">7</text><text x="2" y="23">6</text><text x="2" y="32.5">5</text><text x="2" y="42">4</text><text x="2" y="51.5">3</text><text x="2" y="61">2</text><text x="2" y="70.5">1</text><text x="2" y="80">0</text>
        <text x="20" y="86">2018</text><text x="54" y="86">2019</text><text x="88" y="86">2020</text><text x="122" y="86">2021</text>
      </g>
      <rect x="15" y="69.5" width="5" height="9.5" fill="#7a787f"/><rect x="21" y="69.5" width="5" height="9.5" fill="#4a3570"/><rect x="27" y="65" width="5" height="14" fill="#8a6fc0"/>
      <rect x="49" y="55" width="5" height="24" fill="#7a787f"/><rect x="55" y="50.5" width="5" height="28.5" fill="#4a3570"/><rect x="61" y="60" width="5" height="19" fill="#8a6fc0"/>
      <rect x="83" y="45.5" width="5" height="33.5" fill="#7a787f"/><rect x="89" y="41" width="5" height="38" fill="#4a3570"/><rect x="95" y="31.5" width="5" height="47.5" fill="#8a6fc0"/>
      <rect x="117" y="41" width="5" height="38" fill="#7a787f"/><rect x="123" y="27" width="5" height="52" fill="#4a3570"/><rect x="129" y="12.5" width="5" height="66.5" fill="#8a6fc0"/>
    </svg>
    <div class="point" style="top:47px;background:#8f8c95"><span class="sq" style="background:#fff"></span><b>Heading I</b><i>35 Time exploring</i></div>
    <div class="point" style="top:77px;background:#57447f"><span class="sq"></span><b>Heading II</b><i>45 Time exploring</i></div>
    <div class="point" style="top:107px;background:#8a6fc0"><span class="sq"></span><b>Heading III</b><i>55 Time exploring</i></div>
  </section>

  <!-- 19 Map -->
  <section class="slide">
    <div class="rail"><span class="mark"></span><span class="line"></span><span class="dot"></span></div>
    <h2 class="title center" style="top:17px">United States Map Infographic</h2>
    <div class="ph" role="img" aria-label="Map of the United States divided into states" style="left:34px;top:43px;width:130px;height:77px;border-radius:12px 18px 24px 30px;background:linear-gradient(160deg,#6a686f,#4a4850)"></div>
    <div class="abs" style="left:50px;top:44px;width:20px;height:20px;border-radius:50%;background:#2a2930;font-size:4.2px;display:flex;align-items:center;justify-content:center">82%</div>
    <div class="abs" style="left:106px;top:66px;width:20px;height:20px;border-radius:50%;background:#6a559a;font-size:4.2px;display:flex;align-items:center;justify-content:center">34%</div>
    <div class="abs" style="left:58px;top:81px;width:20px;height:20px;border-radius:50%;background:#5a4685;font-size:4.2px;display:flex;align-items:center;justify-content:center">55%</div>
    <div class="abs" style="left:126px;top:99px;width:20px;height:20px;border-radius:50%;background:#4a3a6a;font-size:4.2px;display:flex;align-items:center;justify-content:center">20%</div>
    <div class="abs" style="left:40px;top:123px;width:96px;height:24px;background:#fff;font-size:3px;color:var(--purple)">
      <span class="abs" style="left:6px;top:6px">☑ Service</span><span class="abs" style="left:52px;top:6px">☑ Automotive</span>
      <span class="abs" style="left:6px;top:15px">☑ Display</span><span class="abs" style="left:52px;top:15px">☑ Display</span>
    </div>
    <p class="abs" style="left:178px;top:74px;font-size:4.8px">YOUR TEXT HERE</p>
    <p class="abs tiny" style="left:178px;top:82px;width:94px;color:#c9c7cf;line-height:4.2px">Show where members are active across the country and share the reach of each project with a short note here.</p>
    <p class="abs tiny" style="left:178px;top:104px;width:94px;color:var(--purple);line-height:3.6px;font-size:2.6px">"ADD A SHORT QUOTE FROM A MEMBER ABOUT THEIR REGION"</p>
  </section>

  <!-- 20 Vector Infographic -->
  <section class="slide">
    <div class="rail"><span class="mark"></span><span class="line"></span><span class="dot"></span></div>
    <h2 class="abs" style="left:31px;top:17px;font-size:9px;font-weight:300;line-height:10px">Vector<br>Infographic Slide</h2>
    <div class="ph" role="img" aria-label="Winding road with two cars and location pins" style="left:120px;top:15px;width:159px;height:142px;background:linear-gradient(200deg,#0a0a0c 20%,#3a3a40 60%,#5a5a62 100%)"></div>
    <div class="proc" style="top:68px;width:43px;background:var(--grey)">PROCESS 01</div>
    <p class="abs tiny" style="left:32px;top:76px;width:88px;color:#c9c7cf;line-height:3.6px">Describe the first step of the plan in a short and clear line.</p>
    <div class="proc" style="top:92px;width:36px;background:var(--plum)">PROCESS 02</div>
    <p class="abs tiny" style="left:32px;top:100px;width:88px;color:#c9c7cf;line-height:3.6px">Describe the second step of the plan in a short and clear line.</p>
    <div class="proc" style="top:116px;width:43px;background:var(--purple)">PROCESS 03</div>
    <p class="abs tiny" style="left:32px;top:124px;width:88px;color:#c9c7cf;line-height:3.6px">Describe the third step of the plan in a short and clear line.</p>
  </section>

  <!-- 21 Thank You -->
  <section class="slide">
    <div class="ph" role="img" aria-label="Black hole with a glowing golden accretion disk among stars" style="inset:0;background:radial-gradient(ellipse at 50% 45%,#000 10%,#6a5a7a 22%,#2a3050 40%,#0c1020 75%)"></div>
    <div class="ring" style="left:131px;top:22px;width:16px;height:16px"></div>
    <h2 class="abs" style="left:0;right:0;top:60px;text-align:center;font-size:21px;font-weight:800">Thank You</h2>
    <ul class="abs" style="left:113px;top:106px;list-style:none;font-size:2.8px;line-height:6px">
      <li><svg width="4" height="4" viewBox="0 0 10 10" style="margin-right:6px"><path d="M5 0a3.5 3.5 0 0 0-3.5 3.5C1.5 6 5 10 5 10s3.5-4 3.5-6.5A3.5 3.5 0 0 0 5 0z" fill="#fff"/></svg>Your address goes here</li>
      <li><svg width="4" height="4" viewBox="0 0 10 10" style="margin-right:6px"><circle cx="5" cy="5" r="4.3" fill="none" stroke="#fff"/><path d="M1 5h8M5 1v8" stroke="#fff"/></svg>www.thelantern.org</li>
      <li><svg width="4" height="4" viewBox="0 0 10 10" style="margin-right:6px"><rect x="0.5" y="2" width="9" height="6" fill="#fff"/></svg>hello@thelantern.org</li>
      <li><svg width="4" height="4" viewBox="0 0 10 10" style="margin-right:6px"><path d="M2 1l2 2-1 1.5c1 2 2 3 3.5 3.5L8 6.5l2 2L8.5 10C4 9 1 6 0 1.5z" fill="#fff"/></svg>+00 2412 XXXX XXXX</li>
    </ul>
  </section>

</main>
</body>
</html>
```